Book cover for a sci fi book called The Velvet Assembly

Dear Pixel Harbor team,

I would need a book cover design for my sci fi book, 'The Velvet Assembly'.

I will start by briefing you about the book's content, then I would like to advice you about a few possible book cover scenarios that I could imagine having for the book, and on which I would like to ask you to work on.

Book abstract:

The velvet assembly is a technically developed and spiritually evolved society from a distant galaxy.

Main location the actions take place: Planet Earth, globalized world, former Northern Germany, a new isolated high tech city at the sea, called Lees, inhabitants from everywhere, one government, one religion.
• Year: 2093
• The Velvet Assembly: solar system with 7 suns. The inhabitans of the velvet assembly have no physical body, only energetical bodies. Only when visiting Earth, they can incarnate at will.

The action starts on planet Earth, where a group of 4 people, two women and two males, who meet through different circumstances and decide to follow together a spiritual and philiosophical path towards self development and evolution. They meet an incarnated master from the velvet assembly who leads their path. At the end of the books, they reach a form of enlightment and transcende to The Velvet Assembly, they only come to know at the end the truth about the real origin of their master.

For the book cover, no matter what ideas you choose, please use max three predominant colors for that, red, yellow and orange. The book cover should inspire warmth.

Suggestions for the design:
- an abstract sun
- a cosmic view of the velvet assembly
- an abstractized design of a sacred geometry shape
- sun in the upper left corner, shining with visible rays on the whole surface of the book cover, a group of 4 people with the female old master sitting by their side in the lower right corner
- an out of the box Ufo, please choose for example an asymmetrical shape, definately not the usual flying sorcer, departing from the velvet assembly solar system, cosmic view from above
- PLEASE FEEL FREE TO BRAINSTROM ON YOUR OWN IDEAS BASED ON WHAT THE BOOK ABSTRACT INSPIRED YOU

For any questions, I am atbyour disposal.

I am looking forward to your design, thank you in advance for that.

Kind regards,
Mira

Target Market(s)

Sci Fi enthusiasts
Philosophers

Font styles to use
Serif

Colors
fbee3e
ffc214
faa54b
f37122
f04a50

Requirements
Must have
• For the book cover, no matter what ideas you choose, please use max three predominant colors for that, red, yellow and orange and/or any derived hues. The book cover should inspire warmth.
• Suggestions for the design:
• - an abstract sun
• - a cosmic view of the velvet assembly
• - an abstractized design of a sacred geometry shape
• - sun in the upper left corner, shining with visible rays on the whole surface of the book cover, a group of 4 people with the female old master sitting by their side in the lower right corner
• - an out of the box Ufo, please choose for example an asymmetrical shape, definately not the usual flying sorcer, departing from the velvet assembly solar system, cosmic view from above
• - PLEASE FEEL FREE TO BRAINSTROM ON YOUR OWN IDEAS BASED ON WHAT THE BOOK ABSTRACT INSPIRED YOU
Nice to have
• Minimalistic and modern design
Should not have
• dark or grey shades
• phtographs

```html
<!DOCTYPE html>
<html lang="en">
<head>
<meta charset="utf-8">
<title>The Velvet Assembly — Book Cover</title>
<link rel="stylesheet" href="https://fonts.googleapis.com/css2?family=Playfair+Display:wght@400;500&display=swap">
<style>
  :root {
    --sky-red: #f34a58;
    --ground-yellow: #fbea3e;
    --sun-gold: #ffc214;
    --ember-orange: #faa54b;
    --deep-orange: #f37122;
    --title-shadow: #e8232f;
    --author-shadow: #f37122;
    --text-white: #ffffff;
  }
  html, body {
    margin: 0;
    padding: 0;
    width: 900px;
    height: 1200px;
    overflow: hidden;
    background: var(--ground-yellow);
  }
  .cover {
    position: relative;
    width: 900px;
    height: 1200px;
    overflow: hidden;
    background: var(--ground-yellow);
    font-family: "Playfair Display", Georgia, serif;
  }
  .sky {
    position: absolute;
    left: 0; top: 0;
    width: 900px;
    height: 736px;
    background: var(--sky-red);
  }
  .ground {
    position: absolute;
    left: 0; top: 736px;
    width: 900px;
    height: 464px;
    background: radial-gradient(ellipse at 30% 40%, #fcef55 0%, var(--ground-yellow) 55%, #f8e23a 100%);
  }
  .sun {
    position: absolute;
    left: 64px;
    top: 50px;
    width: 404px;
    height: 404px;
    border-radius: 50%;
    background: radial-gradient(circle at 40% 40%, #ffc82a 0%, var(--sun-gold) 70%, #fbb813 100%);
  }
  .shards {
    position: absolute;
    left: 470px;
    top: 636px;
    width: 345px;
    height: 320px;
    background: linear-gradient(180deg, var(--text-white) 0%, var(--text-white) 40%, var(--ember-orange) 52%, rgba(250,165,75,0) 100%);
    opacity: 0.85;
  }
  .title {
    position: absolute;
    left: 0;
    top: 0;
    width: 900px;
    margin: 0;
    color: var(--text-white);
    font-weight: 400;
    text-transform: uppercase;
    text-shadow: 3px 3px 0 var(--title-shadow);
  }
  .title span {
    position: absolute;
    display: block;
    line-height: 1;
    white-space: nowrap;
  }
  .title .the {
    left: 337px;
    top: 170px;
    font-size: 112px;
  }
  .title .velvet {
    left: 0;
    width: 900px;
    text-align: center;
    top: 280px;
    font-size: 168px;
  }
  .title .assembly {
    left: 0;
    width: 900px;
    text-align: center;
    top: 420px;
    font-size: 150px;
    letter-spacing: -2px;
  }
  .author {
    position: absolute;
    left: 0;
    top: 1003px;
    width: 900px;
    margin: 0;
    text-align: center;
    color: var(--text-white);
    font-weight: 400;
    font-size: 116px;
    line-height: 1;
    letter-spacing: -2px;
    white-space: nowrap;
    text-shadow: 3px 3px 0 var(--author-shadow);
  }
</style>
</head>
<body>
  <main class="cover">
    <div class="sky"></div>
    <div class="ground"></div>
    <div class="sun"></div>
    <div class="shards" role="img" aria-label="Illustration of five slender white spires dipping into the yellow ground, fading into orange reflections"></div>
    <h1 class="title">
      <span class="the">The</span>
      <span class="velvet">Velvet</span>
      <span class="assembly">Assembly</span>
    </h1>
    <p class="author">Author Name</p>
  </main>
</body>
</html>
```